Poster Design Project

We are a pizzeria based in Sydney CBD. Please see attached file for new website, do not use the current website look to make your graphic design.

We want to run a promotional campaign called " Rustico Rush".

Rustico Rush
$9 Pizza

Crispy & fresh dough topped with mouth watering mozzarella cheese, sprinkled with oregano and finished with fresh basil.

takeaway & eat in only
Medium Pizza Only (11 inch)

Target Market(s)

It is the lunch crowd in sydney cbd, predominately male but some female too. targeting the office workers.

Industry/Entity Type

Graphic Design

Requirements
Must have
• We are an Italian Pizzeria, so we would like an italian look and feel
our unique advantage is authentic and delicious thin crispy pizza
we want a nostalgic look and feel
some examples are attached of colours and style we like
Nice to have
• I can send you via email files to show you what the new website will look like

```html
<!DOCTYPE html>
<html lang="en">
<head>
<meta charset="utf-8">
<title>Rustico Rush — $9 Pizza</title>
<link href="https://fonts.googleapis.com/css2?family=Rubik+Dirt&family=Kaushan+Script&display=swap" rel="stylesheet">
<style>
  :root {
    --cream: #f3ecdc;
    --cream-light: #fffdf6;
    --red: #d11f2a;
    --red-deep: #b3121d;
    --green: #17873a;
    --green-deep: #0e6b2c;
    --ink: #1d1a18;
    --crust: #d9a15a;
    --cheese: #efe09a;
    --basil: #3f7a24;
  }
  * { margin: 0; padding: 0; box-sizing: border-box; }
  html, body { width: 848px; height: 1200px; overflow: hidden; background: var(--cream); }
  .poster {
    position: relative;
    width: 848px;
    height: 1200px;
    overflow: hidden;
    background: radial-gradient(circle at 640px 470px, var(--cream-light) 0, var(--cream) 380px, #eadfc6 100%);
    font-family: "Rubik Dirt", "Impact", sans-serif;
  }
  .shape { position: absolute; left: 0; top: 0; }
  .photo { position: absolute; }
  .photo--top {
    left: -30px; top: -20px; width: 360px; height: 270px;
    border-radius: 0 0 50% 50% / 0 0 45% 45%;
    background: radial-gradient(ellipse at 45% 40%, var(--cheese) 0, #c9b36a 45%, var(--crust) 75%, #f2ece0 90%);
  }
  .photo--bottom {
    left: 430px; top: 640px; width: 460px; height: 400px;
    border-radius: 50% 0 0 50% / 45% 0 0 55%;
    background: radial-gradient(ellipse at 60% 45%, var(--cheese) 0, #b7ad5c 40%, var(--basil) 55%, #e0c07a 72%, var(--crust) 88%);
  }
  .title {
    position: absolute; left: 62px; top: 250px;
    color: var(--red);
    font-size: 138px; line-height: 0.86;
    letter-spacing: 2px;
    text-shadow: 4px 5px 6px rgba(0,0,0,0.35);
  }
  .description {
    position: absolute; left: 80px; top: 512px;
    color: var(--ink);
    font-size: 19px; line-height: 27px;
    font-variant: small-caps;
    letter-spacing: 1px;
  }
  .amp { font-family: "Kaushan Script", cursive; font-variant: normal; }
  .price {
    position: absolute; left: 62px; top: 630px;
    color: var(--green);
    font-size: 132px; line-height: 1;
    text-shadow: 3px 4px 5px rgba(0,0,0,0.3);
  }
  .service {
    position: absolute; left: 64px; top: 780px;
    color: var(--ink);
    font-size: 86px; line-height: 0.95;
    text-shadow: 2px 3px 4px rgba(255,255,255,0.5);
  }
  .service .amp { font-size: 56px; vertical-align: 24px; margin-left: 4px; }
  .size-note {
    position: absolute; left: 78px; top: 1060px;
    color: var(--cream);
    font-size: 32px; letter-spacing: 1px;
    font-variant: small-caps;
  }
</style>
</head>
<body>
<main class="poster">
  <svg class="shape" width="848" height="1200" viewBox="0 0 848 1200" aria-hidden="true">
    <path fill="var(--green)" d="M640 0 H848 V490 L820 485 L790 470 L772 440 L770 330 L780 300 L770 270 L740 250 L700 240 L660 210 L640 160 L632 100 L628 40 Z"/>
    <path fill="var(--red)" d="M0 960 L60 945 L130 955 L220 930 L300 955 L380 945 L470 975 L560 995 L650 1020 L760 1050 L740 1110 H0 Z"/>
    <path fill="var(--ink)" d="M0 1110 H760 L800 1090 L848 1060 V1200 H0 Z"/>
  </svg>

  <div class="photo photo--top" role="img" aria-label="Photo of a margherita pizza with basil and oregano"></div>
  <div class="photo photo--bottom" role="img" aria-label="Close-up photo of a margherita pizza slice with basil pesto"></div>

  <h1 class="title">RUSTICO<br>RUSH</h1>

  <p class="description">
    Crispy <span class="amp">&amp;</span> fresh dough topped<br>
    with mouth watering mozzarella cheese,<br>
    sprinkled with oregano<br>
    and finished with fresh basil.
  </p>

  <p class="price">$9 PIZZA</p>

  <p class="service">TAKEAWAY<span class="amp">&amp;</span><br>EAT IN ONLY</p>

  <p class="size-note">Medium Pizza Only (11 inch)</p>
</main>
</body>
</html>
```